New Business Card Design For Re-Branded Company (New Logo)

We recently switched our DBA and had a new logo designed. We now need new business cards made around our new logo. We would like to stick with the color scheme in our logo: White, Orange, and Blue. We want to see original bold designs that reflect our position in the solar energy sector but we prefer simple over complicated.

We are curious about vertical designs so if you can translate your design onto a vertical layout we would be open to look at it. We especially like a few designs we have seen on here that are vertical with a black or very dark gray background. They have our logo on one side and then the normal vertical business card on the other side.

I have included a screenshot of one of the samples we like, labeled sample.jpg and a file we were given as an example of our logo on a dark background.

At the same time we are satisfied to stay with what we have always had in a horizontal format. If it's not a lot of extra work for you, designs that are submitted in both horizontal and vertical formats will be greatly appreciated.

Please submit your original, bold, clean designs for consideration. Contact us with any questions or comments that may arise.

Thank you and Good Luck,

KP

```html
<!DOCTYPE html>
<html lang="en">
<head>
<meta charset="utf-8">
<title>Kestrel Power – Vertical Business Card</title>
<link rel="stylesheet" href="https://fonts.googleapis.com/css2?family=Open+Sans:wght@400;600;700&display=swap">
<style>
  :root {
    --page: #e9e6e1;
    --card-dark: #050505;
    --card-mid: #120c08;
    --orange: #f07a22;
    --blue: #1f7fd0;
    --white: #ffffff;
  }
  * { margin: 0; padding: 0; box-sizing: border-box; }
  html, body { width: 1200px; height: 892px; overflow: hidden; }
  body {
    background: var(--page);
    font-family: "Open Sans", Verdana, sans-serif;
    color: var(--white);
    position: relative;
  }
  .card {
    position: absolute;
    top: 96px;
    width: 400px;
    height: 700px;
    background: linear-gradient(160deg, var(--card-dark) 0%, var(--card-mid) 55%, var(--card-dark) 100%);
    border-radius: 4px;
    box-shadow: 0 12px 30px rgba(0,0,0,.25);
    overflow: hidden;
  }
  .card--front { left: 150px; }
  .card--back { left: 650px; }

  .brand {
    display: flex;
    align-items: center;
    justify-content: center;
    gap: 12px;
  }
  .brand__dot {
    width: 34px; height: 34px;
    border-radius: 50%;
    background: var(--blue);
    flex: none;
  }
  .brand__name {
    font-weight: 700;
    font-size: 30px;
    letter-spacing: 1px;
    color: var(--orange);
    text-transform: uppercase;
    white-space: nowrap;
  }

  .card--front .brand { margin-top: 120px; }
  .person { text-align: center; margin-top: 46px; }
  .person__name { font-size: 34px; font-weight: 600; color: var(--orange); letter-spacing: 1px; }
  .person__role { font-size: 19px; margin-top: 2px; letter-spacing: .5px; }

  .address { text-align: center; margin-top: 38px; font-size: 18px; line-height: 1.45; letter-spacing: .5px; }

  .contacts { list-style: none; margin: 36px auto 0; width: 220px; font-size: 18px; letter-spacing: .8px; }
  .contacts li { display: flex; align-items: center; gap: 14px; line-height: 1.7; }
  .contacts svg { width: 16px; height: 16px; flex: none; }
  .email { text-align: center; margin-top: 28px; font-size: 19px; letter-spacing: .6px; }

  .card--back .brand { margin-top: 300px; }
  .web { text-align: center; margin-top: 86px; font-size: 20px; letter-spacing: 1px; }
</style>
</head>
<body>
  <section class="card card--front">
    <div class="brand">
      <span class="brand__dot"></span>
      <span class="brand__name">Kestrel Power</span>
    </div>
    <div class="person">
      <p class="person__name">Dana Reyes</p>
      <p class="person__role">President</p>
    </div>
    <p class="address">PO Box 3127<br>Riverton Vale NSW 2099</p>
    <ul class="contacts">
      <li>
        <svg viewBox="0 0 16 16" aria-hidden="true"><rect width="16" height="16" rx="2" fill="var(--orange)"/><path d="M5 3.5l2 2-1 1.2c.6 1.3 1.7 2.4 3 3l1.2-1 2 2-1.3 1.6C7.6 12 4 8.4 3.5 5z" fill="#000"/></svg>
        <span>94 3181 2760</span>
      </li>
      <li>
        <svg viewBox="0 0 16 16" aria-hidden="true"><rect width="16" height="16" rx="2" fill="var(--orange)"/><rect x="5" y="3" width="6" height="10" rx="1" fill="#000"/></svg>
        <span>74 2093 6615</span>
      </li>
      <li>
        <svg viewBox="0 0 16 16" aria-hidden="true"><rect width="16" height="16" rx="2" fill="var(--orange)"/><rect x="3" y="6" width="10" height="6" rx="1" fill="#000"/><rect x="5" y="3.5" width="6" height="3" fill="#000"/></svg>
        <span>94 7320 4158</span>
      </li>
    </ul>
    <p class="email">kestrelpower@email.com</p>
  </section>

  <section class="card card--back">
    <div class="brand">
      <span class="brand__dot"></span>
      <span class="brand__name">Kestrel Power</span>
    </div>
    <p class="web">www.kestrelpower.com</p>
  </section>
</body>
</html>
```